11x 11 - KIVO Program Flyer

Introducing The KIVO PROGRAM

The BEST DPA Product on the Planet
* Lowest Zarn in the Industry - 580 Minimum
* Nothing Down - 100% GTU Purchase Financing
* One Submission, One Approval and One Closing
* No Income Limits, No DTI Restrictions, No Property Restrictions

Call (800) 471-9026 for more information

RLCB #738160
www.2ndlanehomes.com

```html
<!DOCTYPE html>
<html lang="en">
<head>
<meta charset="UTF-8">
<title>KIVO Program Flyer</title>
<link rel="stylesheet" href="https://fonts.googleapis.com/css2?family=Montserrat:ital,wght@0,200;0,300;0,400;0,500;0,600;0,700;0,800;0,900;1,200;1,300;1,800;1,900&display=swap">
<style>
  :root {
    --green: #9fcb3b;
    --ink: #2f2f33;
    --white: #ffffff;
    --sky-blue: #cfe0ee;
    --khaki: #d9d39d;
  }
  * { margin: 0; padding: 0; box-sizing: border-box; }
  html, body { width: 1200px; height: 1200px; overflow: hidden; }
  body { font-family: "Montserrat", sans-serif; background: var(--white); }
  .flyer { position: relative; width: 1200px; height: 1200px; overflow: hidden; }

  .hero-photo {
    position: absolute; inset: 0;
    background: linear-gradient(160deg, #a9b4c2 0%, #8a95a3 35%, #6e6a66 65%, #4e4a47 100%);
  }
  .shapes { position: absolute; inset: 0; }

  .brand {
    position: absolute; top: 62px; right: 40px;
    display: flex; align-items: center; gap: 8px;
    font-weight: 700; font-size: 15px; color: var(--white);
  }
  .brand-dot { width: 12px; height: 12px; border-radius: 50%; background: var(--green); }

  .intro {
    position: absolute; left: 52px; top: 497px;
    transform: rotate(-90deg); transform-origin: left top;
    font-weight: 300; font-size: 50px; letter-spacing: 1px;
    color: var(--white); line-height: 1; white-space: nowrap;
  }
  .title { position: absolute; left: 100px; line-height: 1; white-space: nowrap; }
  .title-the { top: 112px; font-weight: 900; font-size: 94px; color: var(--green); letter-spacing: -2px; }
  .title-name { top: 184px; left: 96px; font-weight: 900; font-size: 200px; color: var(--green); letter-spacing: -6px; }
  .title-program { top: 345px; left: 114px; font-weight: 800; font-size: 132px; color: var(--white); letter-spacing: -3px; }
  .tagline {
    position: absolute; left: 118px; top: 460px;
    font-weight: 200; font-size: 36px; color: var(--white); white-space: nowrap; line-height: 1;
  }

  .couple-photo {
    position: absolute; left: 137px; top: 646px;
    width: 422px; height: 262px;
    transform: rotate(-14deg);
    background: var(--white); padding: 14px;
    box-shadow: 0 6px 18px rgba(0,0,0,0.25);
  }
  .couple-photo-fill {
    width: 100%; height: 100%;
    background: linear-gradient(180deg, #e9e9e6 0%, #d5d3cf 55%, #b89a74 100%);
  }

  .pitch { position: absolute; left: 699px; line-height: 1; white-space: nowrap; color: var(--green); }
  .pitch-best { top: 628px; font-weight: 500; font-size: 56px; }
  .pitch-product { top: 676px; font-weight: 900; font-style: italic; font-size: 80px; }
  .pitch-planet { top: 746px; font-weight: 200; font-style: italic; font-size: 58px; }

  .feature { position: absolute; color: var(--ink); line-height: 1; white-space: nowrap; }
  .feature-label { font-weight: 700; font-size: 25px; }
  .feature-big { font-weight: 900; font-style: italic; font-size: 52px; }
  .feature-sub { font-weight: 500; font-size: 24px; }
  .feature-small { font-weight: 500; font-size: 16px; letter-spacing: 0.5px; line-height: 1.3; }

  .contact-pill {
    position: absolute; left: 50px; top: 1050px; width: 236px; height: 46px;
    border-radius: 23px; background: var(--green);
    display: flex; align-items: center; justify-content: center;
    color: var(--white); font-weight: 800; font-style: italic; font-size: 24px;
  }
  .contact-phone {
    position: absolute; left: 18px; top: 1102px;
    font-weight: 900; font-style: italic; font-size: 39px; color: var(--ink); white-space: nowrap;
  }
  .contact-web {
    position: absolute; left: 20px; top: 1158px;
    font-weight: 500; font-size: 17px; color: var(--ink); letter-spacing: 0.5px;
  }
</style>
</head>
<body>
<main class="flyer">
  <div class="hero-photo" role="img" aria-label="Photo of a modern apartment building with glass balconies against a cloudy sky, bare tree branches at left"></div>

  <svg class="shapes" width="1200" height="1200" viewBox="0 0 1200 1200" aria-hidden="true">
    <polygon points="168,845 1200,366 1200,1200 0,1200 0,985" fill="var(--white)"/>
    <polygon points="217,1056 1200,534 1200,1200 217,1200" fill="var(--sky-blue)"/>
    <polygon points="0,1006 118,969 609,1200 0,1200" fill="var(--khaki)"/>
  </svg>

  <div class="brand"><span class="brand-dot"></span>2nd Lane Homes</div>

  <div class="intro">INTRODUCING</div>
  <div class="title title-the">THE</div>
  <div class="title title-name">KIVO</div>
  <div class="title title-program">PROGRAM</div>
  <div class="tagline">WHEN “NOTHING” IS ALL YOU NEED</div>

  <div class="couple-photo">
    <div class="couple-photo-fill" role="img" aria-label="Photo of a happy couple on a sofa raising their arms among moving boxes"></div>
  </div>

  <div class="pitch pitch-best">THE BEST DPA</div>
  <div class="pitch pitch-product">PRODUCT</div>
  <div class="pitch pitch-planet">ON THE PLANET</div>

  <div class="feature feature-label" style="left:706px;top:820px;">LOWEST ZARN IN THE INDUSTRY</div>
  <div class="feature feature-big" style="left:700px;top:846px;">580 MINIMUM</div>

  <div class="feature feature-label" style="left:706px;top:926px;">NOTHING DOWN</div>
  <div class="feature feature-big" style="left:704px;top:948px;">100% GTU</div>
  <div class="feature feature-sub" style="left:706px;top:998px;">PURCHASE FINANCING</div>

  <div class="feature feature-big" style="left:1008px;top:923px;">ONE</div>
  <div class="feature feature-small" style="left:1010px;top:970px;">SUBMISSION<br>APPROVAL<br>CLOSING</div>

  <div class="feature feature-big" style="left:704px;top:1049px;">WITHOUT</div>
  <div class="feature feature-sub" style="left:706px;top:1101px;font-size:19px;line-height:1.3;">INCOME LIMITS<br>DTI RESTRICTIONS<br>PROPERTY RESTRICTIONS</div>

  <div class="contact-pill">CONTACT US</div>
  <div class="contact-phone">(800) 471-9026</div>
  <div class="contact-web">WWW.2NDLANEHOMES.COM</div>
</main>
</body>
</html>
```